Business card design - landscaping industry

Hello! We are very creative when it comes to landscape design but when it comes to designing business cards - not so much. We could use some help to come up with a design which is professional but fun. We are based in Grand Rapids, MI and work with high end properties for new landscape design and install. We are looking to have a template made for business card for a couple of us on staff.

You can get the flavor of our color scheme from our attached logo. We probably would want to highlight the green but also include some of the blue maybe.

Target Market(s)

We work with residential homeowners here in West Michigan. Very nice people by and large.

Industry/Entity Type

Landscaping

Contact Information for Business Card

The card should be standard size with round edges maybe?

Font styles to use
Serif
Sans Serif
Decorative

Requirements
Must have
• Must haves:
• 1. Address: 4817 Birchwell Meadow Lane SE, Grand Rapids, Michigan 49582
• 2. Phone: 616.555.0187
• 3. Email: company@larkhollowyard.com
• 4. URL: www.larkhollowyard.com
• 5. Names/Titles: (1) Dennis Harlow, President (2) Tomas Belvin, Director of Field Services
Nice to have
• On the back side of the card, we are thinking it would make sense to have a short listing of services offered...
• Landscape design & installation, Professional lawn maintenance, Spring & fall leaf cleanup, Irrigation system installation & maintenance, Snowplowing, Fertilizer & weed control, Tree maintenance and removal, Landscape bed maintenance
Should not have
• Our hope is that the design won't be too ostentatious. We are looking for professional and attractive.

```html
<!DOCTYPE html>
<html lang="en">
<head>
<meta charset="utf-8">
<title>Business Card – Owen Marsh</title>
<link rel="stylesheet" href="https://fonts.googleapis.com/css2?family=Roboto+Condensed:wght@700&family=Roboto:wght@400&display=swap">
<style>
  :root {
    --card-bg: #1f2022;
    --name-blue: #2b82c6;
    --title-green: #3fa550;
    --icon-blue: #2d88cc;
    --text-white: #f4f4f4;
    --divider: #d9d9d9;
  }
  html, body {
    margin: 0;
    padding: 0;
    width: 1200px;
    height: 695px;
    overflow: hidden;
    background: var(--card-bg);
  }
  .card {
    position: relative;
    width: 1200px;
    height: 695px;
    background: var(--card-bg);
    font-family: "Roboto", Arial, sans-serif;
    color: var(--text-white);
  }
  .identity {
    position: absolute;
    right: 577px;
    top: 302px;
    text-align: right;
  }
  .identity__name {
    margin: 0;
    font-family: "Roboto Condensed", "Arial Narrow", sans-serif;
    font-weight: 700;
    font-size: 53px;
    line-height: 1;
    letter-spacing: 0.5px;
    color: var(--name-blue);
    text-transform: uppercase;
  }
  .identity__title {
    margin: 8px 0 0;
    font-size: 29px;
    line-height: 1;
    color: var(--title-green);
    text-transform: uppercase;
    letter-spacing: 0.3px;
  }
  .divider {
    position: absolute;
    left: 649px;
    top: 258px;
    width: 3px;
    height: 184px;
    background: linear-gradient(to bottom, rgba(217,217,217,0), var(--divider) 25%, var(--divider) 75%, rgba(217,217,217,0));
  }
  .contacts {
    position: absolute;
    left: 694px;
    top: 300px;
    margin: 0;
    padding: 0;
    list-style: none;
  }
  .contacts__item {
    display: flex;
    align-items: center;
    height: 36px;
    font-size: 28px;
  }
  .contacts__icon {
    width: 24px;
    height: 24px;
    margin-right: 15px;
    fill: var(--icon-blue);
  }
  .address {
    position: absolute;
    left: 172px;
    top: 573px;
    display: flex;
    align-items: center;
    font-size: 30px;
  }
  .address__icon {
    width: 28px;
    height: 38px;
    margin-right: 10px;
    fill: var(--icon-blue);
  }
</style>
</head>
<body>
<div class="card">
  <div class="identity">
    <h1 class="identity__name">Owen Marsh</h1>
    <p class="identity__title">Director of Field Services</p>
  </div>

  <div class="divider"></div>

  <ul class="contacts">
    <li class="contacts__item">
      <svg class="contacts__icon" viewBox="0 0 24 24" aria-hidden="true"><path d="M6.6 10.8a15.1 15.1 0 0 0 6.6 6.6l2.2-2.2c.3-.3.7-.4 1-.2 1.1.4 2.3.6 3.6.6.6 0 1 .4 1 1V20c0 .6-.4 1-1 1A17 17 0 0 1 3 4c0-.6.4-1 1-1h3.5c.6 0 1 .4 1 1 0 1.3.2 2.5.6 3.6.1.3 0 .7-.2 1z"/></svg>
      <span>616.555.0187</span>
    </li>
    <li class="contacts__item">
      <svg class="contacts__icon" viewBox="0 0 24 24" aria-hidden="true"><path d="M8 1h8a2 2 0 0 1 2 2v18a2 2 0 0 1-2 2H8a2 2 0 0 1-2-2V3a2 2 0 0 1 2-2zm0 3v15h8V4zm4 16.2a1 1 0 1 0 0 .1z"/></svg>
      <span>616.555.0142</span>
    </li>
    <li class="contacts__item">
      <svg class="contacts__icon" viewBox="0 0 24 24" aria-hidden="true"><path d="M12 2a10 10 0 1 0 0 20 10 10 0 0 0 0-20zm-1 17.9A8 8 0 0 1 4.2 10.2L9 15v1a2 2 0 0 0 2 2zm6.9-2.5A2 2 0 0 0 16 16h-1v-3a1 1 0 0 0-1-1H8v-2h2a1 1 0 0 0 1-1V7h2a2 2 0 0 0 2-2v-.4a8 8 0 0 1 2.9 12.8z"/></svg>
      <span>www.larkhollowyard.com</span>
    </li>
  </ul>

  <div class="address">
    <svg class="address__icon" viewBox="0 0 24 32" aria-hidden="true"><path d="M12 1A10 10 0 0 0 2 11c0 7.5 10 20 10 20s10-12.5 10-20A10 10 0 0 0 12 1zm0 14a4 4 0 1 1 0-8 4 4 0 0 1 0 8z"/></svg>
    <span>4817 Birchwell Meadow Lane SE, Grand Rapids, Michigan 49582</span>
  </div>
</div>
</body>
</html>
```